Elegant Black Candle Label Design!

I need a 2.375" tall by 3.0" wide candle label design. I'm looking for simple and elegant. Black label with silver leaf border and lettering. Label needs to have the following information on it: Fern Hollow Candle Co. as the company name, scent name in the middle and in smaller font, it needs to say Made in USA, All Natural, 8oz. Attached photos are for inspiration.

Target Market(s)

People looking for high end, all natural candle fragrances

Industry/Entity Type

Candle-Spa

Colors

Designer to choose only greyscale colors for use in the design.

Requirements
Must have
• Company Name, Scent (ability to change scent names), All Natural, Made in USA, 8oz
Nice to have
• Black background, silver leaf border and silver leaf font. Elegant fonts maybe slightly cursive

```html
<!DOCTYPE html>
<html lang="en">
<head>
<meta charset="utf-8">
<title>Fern Hollow Candle Co. – Lavender Sage Label</title>
<link href="https://fonts.googleapis.com/css2?family=Cormorant+Garamond:wght@400;500&display=swap" rel="stylesheet">
<style>
  :root {
    --page-bg: #eeeeee;
    --label-black: #151515;
    --silver: #d9d9d9;
    --silver-soft: #a8a8a8;
    --leaf-tone: #3a3a3a;
  }
  * { margin: 0; padding: 0; box-sizing: border-box; }
  html, body {
    width: 800px;
    height: 1200px;
    overflow: hidden;
    background: var(--page-bg);
  }
  .canvas {
    position: relative;
    width: 800px;
    height: 1200px;
  }
  .label {
    position: absolute;
    left: 40px;
    top: 315px;
    width: 720px;
    height: 570px;
    background: var(--label-black);
    border-radius: 14px;
    color: var(--silver);
    font-family: "Cormorant Garamond", Georgia, serif;
    text-align: center;
  }
  .frame-outer {
    position: absolute;
    inset: 16px;
    border: 1.5px solid var(--silver-soft);
  }
  .frame-inner {
    position: absolute;
    inset: 30px;
    border: 1.5px solid var(--silver);
  }
  .leaf-spray-side {
    position: absolute;
    left: 40px;
    top: 300px;
    width: 90px;
    height: 180px;
    background: linear-gradient(160deg, var(--leaf-tone), rgba(58,58,58,0.2));
    border-radius: 45px 45px 10px 10px;
  }
  .leaf-spray-bottom {
    position: absolute;
    left: 100px;
    top: 475px;
    width: 210px;
    height: 60px;
    background: linear-gradient(90deg, var(--leaf-tone), rgba(58,58,58,0.15));
    border-radius: 30px;
  }
  .brand-name {
    position: absolute;
    top: 92px;
    left: 0;
    width: 100%;
    font-size: 40px;
    font-weight: 400;
    letter-spacing: 1px;
    color: var(--silver);
  }
  .scent-name {
    position: absolute;
    top: 225px;
    left: 0;
    width: 100%;
    font-size: 64px;
    font-weight: 500;
    letter-spacing: 2px;
  }
  .title-rule {
    position: absolute;
    top: 318px;
    left: 260px;
    width: 200px;
    height: 1.5px;
    background: var(--silver);
  }
  .tagline {
    position: absolute;
    top: 340px;
    left: 0;
    width: 100%;
    font-size: 22px;
  }
  .claims {
    position: absolute;
    top: 385px;
    left: 230px;
    width: 260px;
    height: 90px;
  }
  .claims-rule-top {
    position: absolute;
    top: 0;
    left: 0;
    width: 100%;
    height: 1.5px;
    background: var(--silver);
  }
  .claims-rule-mid {
    position: absolute;
    top: 0;
    left: 129px;
    width: 1.5px;
    height: 90px;
    background: var(--silver);
  }
  .claim {
    position: absolute;
    top: 18px;
    width: 120px;
    font-size: 19px;
    line-height: 1.15;
    letter-spacing: 0.5px;
  }
  .claim-origin { left: 0; }
  .claim-natural { right: 0; }
  .net-weight {
    position: absolute;
    top: 490px;
    left: 0;
    width: 100%;
    font-size: 22px;
    font-weight: 500;
    letter-spacing: 1px;
  }
</style>
</head>
<body>
<div class="canvas">
  <div class="label">
    <div class="frame-outer"></div>
    <div class="frame-inner"></div>
    <div class="leaf-spray-side" role="img" aria-label="Silver fern leaf illustration along the lower left edge"></div>
    <div class="leaf-spray-bottom" role="img" aria-label="Silver fern frond illustration along the bottom edge"></div>

    <div class="brand-name">Fern Hollow Candle Co.</div>
    <h1 class="scent-name">LAVENDER SAGE</h1>
    <div class="title-rule"></div>
    <p class="tagline">Crafted for balance and relaxation.</p>

    <div class="claims">
      <div class="claims-rule-top"></div>
      <div class="claims-rule-mid"></div>
      <p class="claim claim-origin">MADE IN<br>USA</p>
      <p class="claim claim-natural">ALL<br>NATURAL</p>
    </div>

    <p class="net-weight">8 OZ</p>
  </div>
</div>
</body>
</html>
```